Business Card Design Project

Im an electrician and my company name is Brightway Electrical
My main work is installing Lighting and Power Points, Home Theater Systems, TVS, Phones and Data
Im looking a business card, something nice, clean, modern and not to cluttered
Im open to sugestions
I dont mind if the "Services" is on the back on the business card
colours black, grey, white or the blue colour of my logo are prefered but not compulsory
any questions just message me
and please make it so if i need to edit the writing can do it easy. maybe by making it a seperate layer ?
My Details are.
Name - Peter Hollis
Job Title - Licenced Electrician
Mobile - 027 530 2174
Email - peter@brightwayelectrical.co.nz
Web - www.brightwayelectrical.co.nz
Services
Residential / Commercial
Lighting & Power
Heating & Ventilation
Automation
Phone & Data
Home Cinema
Sound Systems
TV, Antenna & Satellite
Digital Upgrades

```html
<!DOCTYPE html>
<html lang="en">
<head>
<meta charset="utf-8">
<title>Brightway Electrical – Business Card</title>
<link rel="stylesheet" href="https://fonts.googleapis.com/css2?family=Open+Sans:wght@400;700&family=Michroma&display=swap">
<style>
  :root {
    --card-black: #1b1b1b;
    --card-white: #ffffff;
    --brand-blue: #00a5c4;
    --text-dark: #1f1f1f;
    --backdrop: #d9d9d9;
  }
  * { margin: 0; padding: 0; box-sizing: border-box; }
  html, body {
    width: 1200px;
    height: 881px;
    overflow: hidden;
    background: var(--backdrop);
    font-family: "Open Sans", Arial, sans-serif;
  }
  .canvas {
    position: relative;
    width: 1200px;
    height: 881px;
  }
  .card {
    position: absolute;
    top: 37px;
    width: 490px;
    height: 798px;
    overflow: hidden;
  }
  /* Back of card */
  .card-back {
    left: 75px;
    background: var(--card-black);
  }
  .card-back .accent-square {
    position: absolute;
    right: 0;
    bottom: 120px;
    width: 200px;
    height: 200px;
    background: var(--brand-blue);
  }
  /* Front of card */
  .card-front {
    left: 641px;
    background: var(--card-white);
  }
  .header-band {
    position: absolute;
    left: 0; top: 0;
    width: 100%;
    height: 202px;
    background: var(--card-black);
  }
  .brand {
    position: absolute;
    right: 40px;
    top: 60px;
    display: flex;
    align-items: center;
    gap: 18px;
  }
  .brand-square {
    width: 62px;
    height: 62px;
    background: var(--brand-blue);
  }
  .brand-name {
    color: var(--brand-blue);
    font-weight: 700;
    font-size: 34px;
    line-height: 40px;
    text-transform: uppercase;
    letter-spacing: 1px;
  }
  .footer-band {
    position: absolute;
    left: 0; bottom: 0;
    width: 100%;
    height: 43px;
    background: var(--card-black);
  }
  .person {
    position: absolute;
    left: 42px;
    top: 477px;
    color: var(--text-dark);
  }
  .person-name {
    font-family: "Michroma", "Open Sans", sans-serif;
    font-size: 22px;
    line-height: 30px;
    letter-spacing: 0.5px;
  }
  .person-title {
    font-size: 20px;
    line-height: 30px;
    margin-top: 3px;
  }
  .contacts {
    position: absolute;
    left: 42px;
    top: 594px;
    list-style: none;
    color: var(--text-dark);
  }
  .contact-item {
    display: flex;
    align-items: center;
    gap: 9px;
    height: 45px;
    font-size: 21px;
  }
  .contact-icon {
    width: 29px;
    height: 29px;
    flex: none;
  }
</style>
</head>
<body>
<main class="canvas">
  <section class="card card-back" aria-label="Card back">
    <div class="accent-square"></div>
  </section>

  <section class="card card-front" aria-label="Card front">
    <header class="header-band">
      <div class="brand">
        <div class="brand-square"></div>
        <div class="brand-name">Brightway<br>Electrical</div>
      </div>
    </header>

    <div class="person">
      <p class="person-name">Peter Hollis</p>
      <p class="person-title">Licenced Electrician</p>
    </div>

    <ul class="contacts">
      <li class="contact-item">
        <svg class="contact-icon" viewBox="0 0 30 30" aria-hidden="true">
          <rect width="30" height="30" rx="5" fill="#1b1b1b"/>
          <path d="M9 7c1-1 2-1 3 0l2 3c.6 1 .3 2-.5 2.6l-1 .8c.8 2 2.4 3.6 4.2 4.4l.8-1c.6-.8 1.7-1 2.6-.4l3 2c1 .8 1 2 0 3l-1.5 1.5C18 25 6 13 7.5 9z" fill="#fff"/>
        </svg>
        <span>027 530 2174</span>
      </li>
      <li class="contact-item">
        <svg class="contact-icon" viewBox="0 0 30 30" aria-hidden="true">
          <rect width="30" height="30" rx="5" fill="#1b1b1b"/>
          <rect x="6" y="9" width="18" height="13" rx="1.5" fill="none" stroke="#fff" stroke-width="2"/>
          <path d="M6.5 10l8.5 6.5 8.5-6.5" fill="none" stroke="#fff" stroke-width="2"/>
        </svg>
        <span>peter@brightwayelectrical.co.nz</span>
      </li>
      <li class="contact-item">
        <svg class="contact-icon" viewBox="0 0 30 30" aria-hidden="true">
          <rect width="30" height="30" rx="5" fill="#1b1b1b"/>
          <g fill="none" stroke="#fff" stroke-width="1.6">
            <circle cx="15" cy="15" r="8.5"/>
            <ellipse cx="15" cy="15" rx="3.8" ry="8.5"/>
            <path d="M6.5 15h17M8 10.5h14M8 19.5h14"/>
          </g>
        </svg>
        <span>www.brightwayelectrical.co.nz</span>
      </li>
    </ul>

    <footer class="footer-band"></footer>
  </section>
</main>
</body>
</html>
```